Webdesign Tischlerei Wallbusch
Zielgruppe
es handelt sich um eine Tischlerei / Meisterbetrieb
Zielgruppe: private und gwerbliche Kunden
Aufgabenstellung
- die Vielfältigkeit der Produkte aus eigener Herstellung durch Meisterhand soll vermittelt werden
- FixWerk Systemspezialist
- Produktschulungen Kork
- KEINE Kopie der alten Seite
- aufgelockert und modern
- gern mit Elementen in leichter Holzoptik und weichen Rundungen
- Farben modern und in Telen an das Logo angepasst
Vorstellung des Kunden zur Navigationsstruktur:
Navigationsstruktur Website
1. wo arbeiten wir... (in der Werkstatt findet mittlerweile der geringere Anteil der Arbeit statt)
• Bild Werkstatt von außen/Schild
• Mitarbeiter an der Säge
• und/oder Mitarbeiter an der Hobelmaschine
• Gespräch/Planung/Skizzen
• evtl. (gepacktes) Fahrzeug(denn das ist ein wichtiges Arbeitsmittel)
2. was macht uns aus...
• vernünftiges Verhältnis zu den Mitarbeitern, ermöglicht eine kontinuierliche, fachgerechte und qualitativ hochwertige Arbeit an den Projekten
• überwiegend handwerkliche Fertigung
• Verwendung von Materialien und Hölzern- auch aus der Region
• Flexibilität im Umgang mit Arbeitszeit, Material und Leistungen
3. welche Möglichkeiten haben wir....
• „Liste“ mit den Möglichkeiten die wir so haben(z.B. Herstellung und Reparaturen von individuellen Treppen, Möbeln, Türen, Lieferung und Reparatur von Fenstern, verlegen und reparieren von Fußböden wie Hobeldielen, Parkett, Designböden, Carport, Zäune, Tore
• Galerie Projekte mit Beschreibung
• vorher-nachher Bilder mit Beschreibung
4. was sollte Sie interessieren...
• Tipps &Tricks rund ums Holz/Produkte(Fenster Pflegehinweise)
• Termine und Veranstaltungen auch nicht betrieblich
• Empfehlungen (Produkte, Materialien, Pflegemittel -was wir benutzen und gefällt oder ist das dann Werbung?)
5. womit könnten wir ihnen helfen...
• Interaktives Anfrageformular
• Möglichkeit Skizzen hochzuladen, Wünsche zu beschreiben
6. wie erreichen Sie uns...<..

```html
<!DOCTYPE html>
<html lang="de">
<head>
<meta charset="utf-8">
<title>Tischlerei Wallbusch</title>
<link href="https://fonts.googleapis.com/css2?family=Encode+Sans+Semi+Condensed:wght@400;500;600&family=Open+Sans:wght@400;600;700&display=swap" rel="stylesheet">
<style>
:root{
  --blue:#0d5fa6;
  --blue-dark:#0a4d88;
  --ink:#2b2622;
  --text:#4a433d;
  --paper:#f7f5f1;
  --cream:#efe9df;
  --white:#ffffff;
  --espresso:#3a2e22;
  --wood-dark-1:#4a3a2a;
  --wood-dark-2:#3b2d20;
  --wood-light-1:#c79a6a;
  --wood-light-2:#a97a4d;
}
*{box-sizing:border-box;margin:0;padding:0}
html,body{width:1200px;height:4262px;overflow:hidden}
body{position:relative;background:var(--paper);font-family:"Open Sans",sans-serif;color:var(--text)}
.abs{position:absolute}
.heading{font-family:"Encode Sans Semi Condensed","Open Sans",sans-serif;font-weight:500;color:var(--ink)}
.photo{position:absolute;border-radius:14px}
.photo.square{border-radius:0}
.lead{font-size:13.5px;line-height:17px;text-align:center;color:var(--ink)}
.more{font-size:13px;font-weight:700;color:var(--ink);text-decoration:underline;text-underline-offset:3px}
.pill{position:absolute;border-radius:20px;background:var(--blue);color:var(--white);font-weight:700;font-size:13px;display:flex;align-items:center;justify-content:center;box-shadow:0 3px 6px rgba(0,0,0,.25)}

/* header */
.top-strip{left:0;top:0;width:1200px;height:16px;background:var(--espresso)}
.site-header{left:0;top:16px;width:1200px;height:59px;background:var(--paper)}
.brand{left:265px;top:30px;font-family:"Encode Sans Semi Condensed",sans-serif;font-weight:600;font-size:21px;color:var(--blue);letter-spacing:.5px}
.header-phone{left:712px;top:36px;display:flex;align-items:center;gap:8px;font-weight:600;font-size:14px;color:var(--ink)}
.social-dot{left:855px;top:36px;width:22px;height:22px;border:2.5px solid var(--ink);border-radius:50%}
.menu-icon{left:908px;top:38px}

/* hero */
.hero{left:0;top:75px;width:1200px;height:367px;background:var(--espresso)}
.hero-photo{left:480px;top:75px;width:533px;height:367px;background:linear-gradient(90deg,var(--espresso) 0%,#7a5a3e 40%,#b8875a 70%,#6d5138 100%)}
.hero-title{left:265px;top:160px;font-size:26px;color:var(--white);font-weight:500}
.hero-text{left:267px;top:212px;width:240px;font-size:13px;line-height:16.5px;color:var(--white)}
.hero-btn{left:268px;top:328px;width:155px;height:28px;border:1.5px solid #cfc6ba;border-radius:14px;color:var(--white);font-size:12.5px;display:flex;align-items:center;justify-content:center}
.cream-band{left:0;top:442px;width:1200px;height:127px;background:var(--cream)}
.feature{position:absolute;background:var(--paper);border-radius:14px;display:flex;flex-direction:column;align-items:center;text-align:center;font-size:12px;line-height:15px;color:var(--ink);padding-top:10px;box-shadow:0 2px 6px rgba(0,0,0,.08)}
.feature svg{margin-bottom:6px}
.feature.active{background:var(--blue);color:var(--white);box-shadow:0 5px 10px rgba(0,0,0,.3)}

/* possibilities */
.section-white{left:0;top:569px;width:1200px;height:652px;background:var(--white)}
.card-title{font-family:"Encode Sans Semi Condensed",sans-serif;font-weight:500;font-size:20px;line-height:19px;color:var(--ink)}
.card-text{font-size:13px;line-height:17px;color:var(--text);margin:14px 0 16px}
.card{position:absolute;width:210px}

/* wood */
.wood-light-band{left:0;width:1200px;background:repeating-linear-gradient(90deg,var(--wood-light-1) 0 26px,var(--wood-light-2) 26px 34px,#d6ab7c 34px 60px,#b98a5b 60px 70px)}
.wood-dark{left:0;width:1200px;background:repeating-linear-gradient(90deg,var(--wood-dark-1) 0 30px,var(--wood-dark-2) 30px 38px,#55432f 38px 70px,#433425 70px 80px)}

/* work */
.section-paper{left:0;top:2375px;width:1200px;height:558px;background:var(--paper)}

/* interests */
.interest-panel{left:53px;top:3044px;width:1102px;height:581px;background:rgba(244,236,226,.86)}

/* footer */
.foot-box{position:absolute;background:linear-gradient(180deg,#d4aa7a,#c09063);color:var(--white)}
.legal{right:270px;top:4225px;font-size:12px;color:var(--ink);text-transform:uppercase}
</style>
</head>
<body>

<div class="abs top-strip"></div>
<header class="abs site-header"></header>
<div class="abs brand">TISCHLEREI WALLBUSCH</div>
<div class="abs header-phone">
  <svg width="18" height="18" viewBox="0 0 24 24"><path fill="#2b2622" d="M6.6 10.8a15 15 0 0 0 6.6 6.6l2.2-2.2c.3-.3.7-.4 1-.2 1.1.4 2.3.6 3.6.6.6 0 1 .4 1 1V20c0 .6-.4 1-1 1A17 17 0 0 1 3 4c0-.6.4-1 1-1h3.5c.6 0 1 .4 1 1 0 1.3.2 2.5.6 3.6.1.3 0 .7-.2 1z"/></svg>
  030 5550 1234
</div>
<div class="abs social-dot"></div>
<svg class="abs menu-icon" width="22" height="18" viewBox="0 0 22 18"><rect y="1" width="22" height="4" rx="1" fill="#0d5fa6"/><rect y="7" width="22" height="4" rx="1" fill="#0d5fa6"/><rect y="13" width="22" height="4" rx="1" fill="#0d5fa6"/></svg>

<!-- hero -->
<section class="abs hero"></section>
<div class="abs hero-photo" role="img" aria-label="Foto: Hände eines Tischlers beim Hobeln von Holz"></div>
<svg class="abs" style="left:46px;top:220px" width="40" height="70" viewBox="0 0 40 70"><polyline points="36,4 6,35 36,66" fill="none" stroke="#8a8076" stroke-width="6"/></svg>
<svg class="abs" style="left:1114px;top:220px" width="40" height="70" viewBox="0 0 40 70"><polyline points="4,4 34,35 4,66" fill="none" stroke="#8a8076" stroke-width="6"/></svg>
<h1 class="abs heading hero-title">WAS MACHT&nbsp; UNS AUS?</h1>
<p class="abs hero-text">Lorem ipsum dolor sit amet, consectetur adipiscing elit, sed do eiusmod tempor incididunt ut labore et dolore magna aliqua. Quis ipsum suspendisse ultrices gravida.</p>
<div class="abs hero-btn">» mehr über uns</div>

<div class="abs cream-band"></div>
<div class="feature active" style="left:366px;top:394px;width:147px;height:111px">
  <svg width="40" height="38" viewBox="0 0 40 38" fill="none" stroke="#fff" stroke-width="2"><path d="M6 32 26 12M24 6a6 6 0 0 0 8 8l-4 4-8-8z"/><path d="M8 6l26 26M4 10l6-6 4 4-6 6z"/></svg>
  Überwiegend<br>Handwerkliche<br>Fertigung
</div>
<div class="feature" style="left:526px;top:412px;width:149px;height:109px">
  <svg width="40" height="34" viewBox="0 0 40 34" fill="none" stroke="#2b2622" stroke-width="1.8"><circle cx="12" cy="24" r="7"/><circle cx="20" cy="15" r="7"/><circle cx="28" cy="7" r="5"/><path d="M12 17 24 3M17 29 34 10"/></svg>
  Materialien &amp;<br>Hölzer aus der<br>Region
</div>
<div class="feature" style="left:687px;top:412px;width:147px;height:109px">
  <svg width="44" height="34" viewBox="0 0 44 34" fill="none" stroke="#2b2622" stroke-width="1.8"><path d="M2 8h8l8 6 6-4 8 0h10"/><path d="M10 8v12l10 8 4-2 4 2 8-8V8"/><path d="M18 16l6 6M22 14l6 6"/></svg>
  Kunden-<br>orientierte<br>Flexibilität
</div>

<!-- possibilities -->
<section class="abs section-white"></section>
<h2 class="abs heading" style="left:0;width:1240px;top:608px;text-align:center;font-size:33px">Unsere Möglichkeiten</h2>
<p class="abs lead" style="left:360px;width:520px;top:665px">Lorem ipsum dolor sit amet, consectetur adipiscing elit, sed do eiusmod tempor incididunt ut labore et dolore magna aliqua. Quis ipsum suspendisse ultrices gravida. Risus commodo viverra maecenas accumsan lacus vel facilisis.</p>

<div class="photo" style="left:268px;top:761px;width:210px;height:169px;background:linear-gradient(135deg,#3a2b1e,#8a6240 55%,#d9b98a)" role="img" aria-label="Foto: Tischler hobelt ein Werkstück"></div>
<div class="photo" style="left:495px;top:761px;width:208px;height:169px;background:linear-gradient(160deg,#5b3a22,#a0582a 50%,#4a2c18)" role="img" aria-label="Foto: Hand poliert eine Holzoberfläche"></div>
<div class="photo" style="left:722px;top:761px;width:210px;height:169px;background:linear-gradient(135deg,#d8c7b4,#b8987a 50%,#c9a57b)" role="img" aria-label="Foto: Montage eines Scharniers"></div>

<div class="card" style="left:268px;top:955px">
  <div class="card-title">Handwerliche<br>Herstellung</div>
  <p class="card-text">Lorem ipsum dolor sit amet, consectetur adipiscing elit, sed do eiusmod tempor incididunt ut labore et dolore magna aliqua. Quis ipsum suspendisse ultrices gravida.</p>
  <span class="more">» mehr Infos</span>
</div>
<div class="card" style="left:495px;top:955px">
  <div class="card-title">Reparatur und<br>Instandsetzung</div>
  <p class="card-text">Lorem ipsum dolor sit amet, consectetur adipiscing elit, sed do eiusmod tempor incididunt ut labore et dolore magna aliqua. Quis ipsum suspendisse ultrices gravida.</p>
  <span class="more">» mehr Infos</span>
</div>
<div class="card" style="left:722px;top:955px">
  <div class="card-title">Montage</div>
  <p class="card-text">Lorem ipsum dolor sit amet, consectetur adipiscing elit, sed do eiusmod tempor incididunt ut labore et dolore magna aliqua. Quis ipsum suspendisse ultrices gravida.</p>
  <span class="more">» mehr Infos</span>
</div>

<!-- gallery -->
<div class="abs wood-light-band" style="top:1221px;height:58px"></div>
<section class="abs wood-dark" style="top:1279px;height:1096px"></section>
<h2 class="abs heading" style="left:0;width:1162px;top:1341px;text-align:center;font-size:33px;color:#fff">Unsere Galerie</h2>
<p class="abs lead" style="left:360px;width:520px;top:1407px;color:#fff">Lorem ipsum dolor sit amet, consectetur adipiscing elit, sed do eiusmod tempor incididunt ut labore et dolore magna aliqua. Quis ipsum suspendisse ultrices gravida. Risus commodo viverra maecenas accumsan lacus vel facilisis.</p>

<div class="photo square" style="left:99px;top:1501px;width:320px;height:320px;background:linear-gradient(135deg,#e6d2b2,#cfb08a 60%,#b99a76)" role="img" aria-label="Foto: Einbauschrank unter der Dachschräge"></div>
<div class="photo square" style="left:99px;top:1844px;width:320px;height:336px;background:linear-gradient(180deg,#e8dccb,#c7925a 55%,#6f9c97)" role="img" aria-label="Foto: Küche mit Holzarbeitsplatte"></div>
<div class="photo square" style="left:439px;top:1501px;width:321px;height:293px;background:linear-gradient(135deg,#f0e6d6,#dcc6a6 60%,#c9ad86)" role="img" aria-label="Foto: Holztreppe mit Wandschrank"></div>
<div class="photo square" style="left:441px;top:1822px;width:319px;height:434px;background:linear-gradient(180deg,#e4e2dc,#9c5a2a 25%,#8a4a22 80%,#c9c3b9)" role="img" aria-label="Foto: Schrank aus Kirschholz"></div>
<div class="photo square" style="left:778px;top:1501px;width:319px;height:233px;background:linear-gradient(180deg,#7a6a5a,#d08a46 45%,#8a5a32)" role="img" aria-label="Foto: Gartenbank mit Schnitzerei"></div>
<div class="photo square" style="left:778px;top:1756px;width:319px;height:268px;background:linear-gradient(180deg,#6f8a5a,#d8b892 40%,#8a8078)" role="img" aria-label="Foto: Gartentisch mit Bänken"></div>
<div class="pill" style="left:507px;top:2297px;width:184px;height:30px">» weitere Projekte</div>

<!-- work -->
<section class="abs section-paper"></section>
<h2 class="abs heading" style="left:268px;top:2550px;font-size:33px">Wo arbeiten wir?</h2>
<p class="abs" style="left:268px;top:2612px;width:215px;font-size:13px;line-height:17px;color:var(--text)">Lorem ipsum dolor sit amet, consectetur adipiscing elit, sed do eiusmod tempor incididunt ut labore et dolore magna aliqua. Quis ipsum suspendisse ultrices gravida. Risus commodo viverra maecenas accumsan lacus vel facilisis.</p>
<div class="pill" style="left:268px;top:2772px;width:152px;height:30px">» mehr Infos</div>
<div class="photo square" style="left:551px;top:2511px;width:210px;height:351px;background:linear-gradient(180deg,#8a7a66,#3a3a42 40%,#b08864)" role="img" aria-label="Foto: Mitarbeiter in der Werkstatt"></div>
<div class="photo square" style="left:768px;top:2511px;width:162px;height:172px;background:linear-gradient(135deg,#9a8a74,#c8b79c 50%,#6a8a8a)" role="img" aria-label="Foto: Werkstatt mit Maschine"></div>
<div class="photo square" style="left:768px;top:2690px;width:162px;height:172px;background:linear-gradient(180deg,#8a7a6a,#b5966e 50%,#6a5a48)" role="img" aria-label="Foto: Baumstamm auf der Säge"></div>

<!-- interests -->
<div class="abs" style="left:0;top:2933px;width:1200px;height:59px;background:var(--cream)"></div>
<section class="abs wood-light-band" style="top:2992px;height:682px"></section>
<div class="abs interest-panel"></div>
<h2 class="abs heading" style="left:0;width:1254px;top:3100px;text-align:center;font-size:33px">Was sollte Sie interessieren?</h2>

<div class="photo" style="left:268px;top:3164px;width:210px;height:169px;background:linear-gradient(135deg,#7a4a24,#e0a868 55%,#f3d8ae)" role="img" aria-label="Foto: Gestapelte Holzbretter"></div>
<div class="photo" style="left:495px;top:3164px;width:208px;height:169px;background:radial-gradient(circle at 55% 55%,#e8d2b0 0 25%,#9a5a2a 45%,#5a3418)" role="img" aria-label="Foto: Tasse Cappuccino"></div>
<div class="photo" style="left:722px;top:3164px;width:210px;height:169px;background:linear-gradient(135deg,#6a4628,#c8945a 55%,#8a5a32)" role="img" aria-label="Foto: Schnitzwerkzeuge"></div>

<div class="card" style="left:268px;top:3362px">
  <div class="card-title">Tipps &amp; Tricks</div>
  <p class="card-text">Lorem ipsum dolor sit amet, consectetur adipiscing elit, sed do eiusmod tempor incididunt ut labore et dolore magna aliqua. Quis ipsum suspendisse ultrices gravida.</p>
  <span class="more">» mehr Infos</span>
</div>
<div class="card" style="left:495px;top:3362px">
  <div class="card-title">Termine &amp;<br>Veranstaltungen</div>
  <p class="card-text">Lorem ipsum dolor sit amet, consectetur adipiscing elit, sed do eiusmod tempor incididunt ut labore et dolore magna aliqua. Quis ipsum suspendisse ultrices gravida.</p>
  <span class="more">» mehr Infos</span>
</div>
<div class="card" style="left:722px;top:3362px">
  <div class="card-title">Empfehlungen</div>
  <p class="card-text">Lorem ipsum dolor sit amet, consectetur adipiscing elit, sed do eiusmod tempor incididunt ut labore et dolore magna aliqua. Quis ipsum suspendisse ultrices gravida.</p>
  <span class="more">» mehr Infos</span>
</div>

<!-- footer -->
<div class="abs" style="left:0;top:3674px;width:1200px;height:58px;background:var(--cream)"></div>
<footer class="abs wood-dark" style="top:3732px;height:490px"></footer>
<div class="abs wood-light-band" style="top:4210px;height:52px"></div>
<div class="abs" style="left:0;width:1200px;top:3806px;text-align:center;font-family:'Encode Sans Semi Condensed',sans-serif;font-weight:600;font-size:44px;color:#fff;letter-spacing:1px">TISCHLEREI WALLBUSCH</div>

<div class="foot-box" style="left:268px;top:3912px;width:267px;height:216px;padding:22px 22px;font-family:'Encode Sans Semi Condensed',sans-serif;font-size:19px;line-height:24px">
  Meisterbetrieb<br>Tischlerei Wallbusch
  <div style="margin-top:18px">Lindenweg 7<br>12345 Holzdorf</div>
  <div style="margin-top:16px;line-height:22px">
    <div style="display:flex;align-items:center;gap:6px"><svg width="14" height="14" viewBox="0 0 24 24"><path fill="#2b2622" d="M6.6 10.8a15 15 0 0 0 6.6 6.6l2.2-2.2c.3-.3.7-.4 1-.2 1.1.4 2.3.6 3.6.6.6 0 1 .4 1 1V20c0 .6-.4 1-1 1A17 17 0 0 1 3 4c0-.6.4-1 1-1h3.5c.6 0 1 .4 1 1 0 1.3.2 2.5.6 3.6.1.3 0 .7-.2 1z"/></svg>030 5550 1234</div>
    <div style="display:flex;align-items:center;gap:6px"><svg width="14" height="14" viewBox="0 0 24 24"><rect x="6" y="2" width="12" height="7" fill="#2b2622"/><rect x="2" y="10" width="20" height="10" rx="2" fill="#2b2622"/></svg>030 5550 1235</div>
  </div>
</div>
<div class="foot-box" style="left:558px;top:3912px;width:372px;height:216px;padding:16px 34px">
  <div style="font-family:'Encode Sans Semi Condensed',sans-serif;font-size:32px;line-height:33px">Womit können wir<br>Ihnen helfen?</div>
  <p style="font-size:13px;line-height:17px;margin-top:12px">Lorem ipsum dolor sit amet, consectetur adipiscing elit, sed do eiusmod tempor incididunt ut labore et dolore.</p>
</div>
<div class="pill" style="left:594px;top:4075px;width:218px;height:30px">» zum Anfrage-Formular</div>
<div class="abs legal">Impressum | Datenschutz</div>

</body>
</html>
```